"Career in Gradvex" | Poster design

We need a "We are hiring" poster design. We are a construction company based in Croatia and we are looking for 3 categories of construction workers. We want moder, serious and powerful poster . In attachment you can find our logo. The font of a text that is used in logo design is "nexa bold".

At the bottom (or where designer can see it) will be description of general condition. The poster must be simple and clear.

Target Market(s)

Wide range of employment

Industry/Entity Type

Construction Company

Colors

Designer to choose colors to be used in the design.

Requirements
Must have
• The text in poster that will be needed is "Mason/carpenter job", "Steel-bender job" and "Auxiliary worker". This terms may be wrong, but it will be translated in local language. Under all of them will be a short descrtiption row, and one row of salary. This is for all three categories.
• At the bottom (or where designer can see it) will be description of general condition. The poster must be simple and clear.

```html
<!DOCTYPE html>
<html lang="en">
<head>
<meta charset="UTF-8">
<title>Career in Gradvex – We Are Hiring</title>
<link href="https://fonts.googleapis.com/css2?family=Bebas+Neue&family=Montserrat:wght@700&family=Arimo:wght@700&display=swap" rel="stylesheet">
<style>
  :root {
    --page-bg: #ebebeb;
    --poster-bg: #2c2c2f;
    --poster-bg-light: #46464a;
    --accent-yellow: #f6d61a;
    --brand-orange: #ee7d22;
    --ink-dark: #262626;
    --text-white: #ffffff;
    --muted-grey: #8a8a8a;
    --rule: #e8e8e8;
  }
  * { margin: 0; padding: 0; box-sizing: border-box; }
  html, body { width: 847px; height: 1200px; overflow: hidden; background: var(--page-bg); }
  .poster {
    position: absolute; left: 46px; top: 64px; width: 755px; height: 1071px;
    background: var(--poster-bg); overflow: hidden;
  }
  .hero-photo {
    position: absolute; left: 135px; top: 57px; width: 620px; height: 960px;
    background:
      radial-gradient(ellipse at 55% 35%, rgba(90,90,96,0.9) 0%, rgba(60,60,66,0.6) 40%, rgba(44,44,47,0) 75%),
      linear-gradient(180deg, var(--poster-bg-light) 0%, var(--poster-bg) 100%);
  }
  .brand { position: absolute; left: 57px; top: 59px; width: 212px; text-align: center; }
  .brand-square { width: 76px; height: 74px; border: 2px solid #6b6b6b; margin: 0 auto 14px 66px; }
  .brand-name {
    font-family: "Montserrat", sans-serif; font-weight: 700; font-size: 27px;
    color: var(--brand-orange); letter-spacing: 1px; text-align: left;
  }
  .brand-tagline {
    font-family: "Arimo", sans-serif; font-weight: 700; font-size: 8.5px;
    color: var(--muted-grey); text-align: left; letter-spacing: 0.2px; margin-top: 1px;
  }
  .hiring-bubble { position: absolute; left: 50px; top: 320px; width: 340px; height: 320px; }
  .hiring-text {
    position: absolute; left: 57px; top: 395px; width: 290px;
    font-family: "Bebas Neue", sans-serif; color: var(--ink-dark); line-height: 0.9;
  }
  .hiring-text .line-1 { font-size: 68px; padding-left: 38px; }
  .hiring-text .line-1 .small { font-size: 54px; }
  .hiring-text .line-2 { font-size: 104px; padding-left: 20px; }
  .job {
    position: absolute; left: 178px; width: 400px; text-align: center; color: var(--text-white);
  }
  .job-title { font-family: "Bebas Neue", sans-serif; font-size: 38px; line-height: 1; }
  .job-desc, .job-salary {
    font-family: "Arimo", sans-serif; font-weight: 700; font-size: 17.5px; line-height: 1.35;
  }
  .job-desc { color: #f2f2f2; }
  .divider { position: absolute; left: 194px; width: 367px; height: 2px; background: var(--rule); }
  .contact {
    position: absolute; left: 0; top: 1010px; width: 755px; text-align: center;
    font-family: "Bebas Neue", sans-serif; font-size: 40px; color: var(--accent-yellow);
    display: flex; justify-content: center; align-items: center; gap: 4px;
  }
  .contact svg { width: 32px; height: 28px; }
</style>
</head>
<body>
  <main class="poster">
    <div class="hero-photo" role="img" aria-label="Photo of a smiling man in a grey suit and yellow hard hat shouting through a megaphone"></div>

    <header class="brand">
      <div class="brand-square"></div>
      <div class="brand-name">GRADVEX</div>
      <div class="brand-tagline">IZVOĐENJE I VOĐENJE GRAĐEVINSKIH RADOVA</div>
    </header>

    <svg class="hiring-bubble" viewBox="0 0 340 320" aria-hidden="true">
      <path d="M200 70 L258 -8 L270 80 Z" fill="var(--accent-yellow)"/>
      <circle cx="152" cy="155" r="143" fill="var(--accent-yellow)"/>
    </svg>
    <div class="hiring-text">
      <div class="line-1"><span class="small">WE</span> ARE</div>
      <div class="line-2">HIRING</div>
    </div>

    <section class="job" style="top:616px">
      <h2 class="job-title">MASON/CARPENTER JOB</h2>
      <p class="job-desc">of them of them Under all of theof them<br>m will be a short descrtiption row</p>
      <p class="job-salary">Sallery $85000</p>
    </section>
    <div class="divider" style="top:735px"></div>

    <section class="job" style="top:750px">
      <h2 class="job-title">STEEL-BENDER JOB</h2>
      <p class="job-desc">of them of them Under all of theof them<br>m will be a short descrtiption row</p>
      <p class="job-salary">Sallery $85000</p>
    </section>
    <div class="divider" style="top:872px"></div>

    <section class="job" style="top:885px">
      <h2 class="job-title">AUXILIARY WORKER</h2>
      <p class="job-desc">of them of them Under all of theof them<br>m will be a short descrtiption row</p>
      <p class="job-salary">Sallery $85000</p>
    </section>

    <footer class="contact">
      <svg viewBox="0 0 32 28" aria-hidden="true">
        <path d="M2 10 Q16 0 30 10 L27 14 L22 12 L21 8 Q16 6 11 8 L10 12 L5 14 Z" fill="var(--accent-yellow)"/>
        <path d="M9 13 L23 13 L28 26 L4 26 Z" fill="var(--accent-yellow)"/>
        <circle cx="16" cy="19" r="3" fill="var(--poster-bg)"/>
      </svg>
      <span>:12345678910 | EMAIL: JOBS@GRADVEX.COM</span>
    </footer>
  </main>
</body>
</html>
```